Post Card Mailer for QUIK PATH PROSPECTS using new logo

We need a post card designed to send through the USA mail service that will go to new prospective clients.

The post card will introduce me and my new company and try to educate them our on company and services.

The goal is for them to call me or email me so I can have a discussion and try to sell our product.

Our product is a name list of individuals that are looking for consulting / help to determine if they qualify for USA social security benefits and then help to manage the process. We sell this name list to law firms that help these individuals.

Our services are better because we have a better less expensive way to identify people via the internet that want help. Our conversion rate is 15%, so every 100 leads a law firm buys the will obtain 15 customers / clients.

Designer on Logo took alot longer than expected. Also there were two projects that needed to combined into one. Which was done yesterday.

Target Market(s)

Law firms

Font styles to use
Serif
Sans Serif
Script

Colors

Designer to choose colors to be used in the design.

Requirements
Must have
• The size of the mailer should be about 6 by 8 inches.
• Two sides.
• Side 1: With our Logo and key messages we want to communicate.
• Side 2: A space to be used by the USA mail services in lower right, my photo and an introduction by me to our company and why they should buy from my company.
Nice to have
• Images that represent what we do, how we help, and our target market.
Should not have
• Poor taste in images that upset people

```html
<!DOCTYPE html>
<html lang="en">
<head>
<meta charset="utf-8">
<title>Quik Path Prospects – Postcard Mailer</title>
<link rel="stylesheet" href="https://fonts.googleapis.com/css2?family=Oswald:wght@300;400;500;600&display=swap">
<style>
  :root{
    --blue:#1b74c2;
    --blue-dark:#155c9c;
    --charcoal:#2c2c2e;
    --charcoal-deep:#222224;
    --grey:#8c8c8c;
    --paper:#ffffff;
    --stage:#e7e7e9;
    --text-light:#f2f2f2;
  }
  *{box-sizing:border-box;margin:0;padding:0}
  html,body{width:1200px;height:762px;overflow:hidden}
  body{background:var(--stage);font-family:'Oswald',sans-serif;position:relative;color:var(--text-light)}

  .card{position:absolute;top:163px;width:580px;height:435px;background:var(--charcoal);overflow:hidden;box-shadow:0 3px 10px rgba(0,0,0,.25)}
  .card--front{left:13px}
  .card--back{left:607px}

  /* ---------- FRONT ---------- */
  .front-brand{position:absolute;left:22px;top:26px;width:180px;color:var(--blue);font-weight:600;font-size:31px;line-height:1.05;letter-spacing:.5px;text-transform:uppercase}

  .benefit{position:absolute;left:0;width:215px}
  .benefit__banner{height:26px;background:var(--blue);clip-path:polygon(0 0,88% 0,100% 50%,88% 100%,0 100%);padding-left:22px;font-weight:600;font-size:16px;line-height:26px;color:#fff;text-transform:uppercase;letter-spacing:.3px}
  .benefit__list{list-style:none;padding:5px 0 0 22px;font-weight:300;font-size:10.5px;line-height:1.35}
  .benefit__list li::before{content:"— ";}
  .benefit--leads{top:140px}
  .benefit--partner{top:211px}
  .benefit--volume{top:282px}
  .benefit--easy{top:353px}

  .front-header{position:absolute;left:215px;top:0;width:365px;height:104px;background:var(--blue);padding:14px 18px 0 14px;text-align:right;text-transform:uppercase}
  .front-header__lead{font-size:15px;font-weight:400;color:#fff;line-height:1.15}
  .front-header__focus{font-size:21px;font-weight:600;color:var(--charcoal-deep);line-height:1.2}
  .front-header__tail{font-size:13.5px;font-weight:400;color:#fff;line-height:1.25}

  .gallery{position:absolute;left:227px;top:114px;width:342px;height:228px;display:grid;grid-template-columns:1fr 1fr;grid-template-rows:1fr 1fr;gap:8px}
  .gallery__tile{position:relative}
  .gallery__image{position:absolute;inset:0 0 16px 0}
  .gallery__caption{position:absolute;left:0;right:0;bottom:0;height:14px;font-size:9px;font-weight:400;text-align:center;color:#fff;line-height:14px}
  .img-care{background:linear-gradient(135deg,#6f7f55,#a98b63 55%,#4d6fa0)}
  .img-law{background:linear-gradient(135deg,#cfcfcf,#6d6d6d 60%,#3c3c3c)}
  .img-tech{background:linear-gradient(135deg,#0d2f57,#1f86c9 55%,#0c1f3a)}
  .img-growth{background:linear-gradient(135deg,#2c3e55,#4f6683 60%,#26364a)}

  .front-contact{position:absolute;left:215px;top:350px;width:365px;height:85px;background:var(--blue);display:flex;align-items:center;padding:0 16px;gap:14px}
  .front-contact__phone{font-size:27px;font-weight:600;color:#fff;letter-spacing:.5px;white-space:nowrap}
  .front-contact__divider{width:2px;height:40px;background:var(--charcoal-deep)}
  .front-contact__email{font-size:12.5px;font-weight:500;color:#fff;white-space:nowrap}

  /* ---------- BACK ---------- */
  .intro-panel{position:absolute;left:0;top:0;width:330px;height:180px;background:var(--blue);clip-path:polygon(0 0,100% 0,80% 100%,0 100%)}
  .intro-panel__photo{position:absolute;left:14px;top:12px;width:123px;height:153px;background:linear-gradient(160deg,#5a5f68,#2a2d33 70%,#1c1e22)}
  .intro-panel__pitch{position:absolute;left:145px;top:20px;width:165px;font-size:10.5px;line-height:1.5;color:var(--charcoal-deep);text-transform:uppercase}
  .intro-panel__pitch strong{font-weight:600}
  .intro-panel__sign{position:absolute;left:145px;top:128px;color:#fff}
  .intro-panel__name{font-size:13px;font-weight:600}
  .intro-panel__role{font-size:9.5px;font-weight:300;font-style:normal;line-height:1.25}

  .back-brand{position:absolute;right:22px;top:26px;width:220px;color:var(--blue);font-weight:600;font-size:30px;line-height:1.05;text-align:right;text-transform:uppercase;letter-spacing:.5px}

  .test-banner{position:absolute;left:312px;top:125px;width:268px;height:30px;background:var(--blue);clip-path:polygon(0 50%,12% 0,100% 0,100% 100%,12% 100%);font-size:21px;font-weight:500;color:var(--charcoal-deep);line-height:30px;text-align:right;padding-right:18px}
  .growth{position:absolute;right:22px;top:166px;text-align:right;color:#fff;font-weight:400}
  .growth__start{font-size:11px}
  .growth__scale{font-size:15px;line-height:1.35}
  .growth__support{font-size:11px}

  .intro-copy{position:absolute;left:14px;top:196px;width:245px}
  .intro-copy__heading{text-transform:uppercase;font-weight:500;color:var(--blue);font-size:16px;line-height:1.3}
  .intro-copy__heading em{font-style:normal;color:#fff;font-size:22px;font-weight:600}
  .intro-copy__text{margin-top:10px;font-size:9.5px;font-weight:300;line-height:1.35;color:#fff}
  .intro-copy__text p{margin-bottom:10px}

  .mail-zone{position:absolute;left:267px;top:233px;width:313px;height:202px;background:var(--paper);color:#222;padding:12px 12px}
  .mail-zone__address{font-size:8px;line-height:1.35;font-weight:400;font-style:normal}
  .mail-zone__stamp{position:absolute;right:17px;top:11px;width:52px;height:52px;border:1.5px solid #222}
</style>
</head>
<body>

<section class="card card--front" aria-label="Postcard front">
  <div class="front-brand">Quik Path Prospects</div>

  <div class="benefit benefit--leads">
    <div class="benefit__banner">Best Leads, Best Price</div>
    <ul class="benefit__list"><li>Our high conversation rates lowers your client acquisition cost</li><li>Referrals Available</li></ul>
  </div>
  <div class="benefit benefit--partner">
    <div class="benefit__banner">Trusted Partner</div>
    <ul class="benefit__list"><li>Reliability, Dependable, Helpful</li><li>Deep business &amp; process acumen</li></ul>
  </div>
  <div class="benefit benefit--volume">
    <div class="benefit__banner">High Volume</div>
    <ul class="benefit__list"><li>50 years of SSD domain knowledge</li><li>Tested technology capabilities</li></ul>
  </div>
  <div class="benefit benefit--easy">
    <div class="benefit__banner">Quik To Use</div>
    <ul class="benefit__list"><li>Integrate seamlessly into your IT systems</li><li>Tailored campaigns</li></ul>
  </div>

  <header class="front-header">
    <p class="front-header__lead">Let's work together to bring</p>
    <p class="front-header__focus">Social Security Disability</p>
    <p class="front-header__tail">Benefits to those in need and deserving!</p>
  </header>

  <div class="gallery">
    <figure class="gallery__tile">
      <div class="gallery__image img-care" role="img" aria-label="Photo of a family caring for an older woman in a wheelchair outdoors"></div>
      <figcaption class="gallery__caption">Passionate &amp; Helpful</figcaption>
    </figure>
    <figure class="gallery__tile">
      <div class="gallery__image img-law" role="img" aria-label="Photo of a judge's gavel and scales of justice"></div>
      <figcaption class="gallery__caption">Understanding of US Social Security Legal Systems</figcaption>
    </figure>
    <figure class="gallery__tile">
      <div class="gallery__image img-tech" role="img" aria-label="Illustration of hands holding a globe of connected digital devices"></div>
      <figcaption class="gallery__caption">Advanced technology to connect people</figcaption>
    </figure>
    <figure class="gallery__tile">
      <div class="gallery__image img-growth" role="img" aria-label="Illustration of a hand drawing a rising arrow over gears"></div>
      <figcaption class="gallery__caption">Process to provide you the BEST leads</figcaption>
    </figure>
  </div>

  <footer class="front-contact">
    <span class="front-contact__phone">555.014.2273</span>
    <span class="front-contact__divider"></span>
    <span class="front-contact__email">marcus@quikpathprospects.com</span>
  </footer>
</section>

<section class="card card--back" aria-label="Postcard back">
  <div class="intro-panel">
    <div class="intro-panel__photo" role="img" aria-label="Portrait photo of the company president"></div>
    <p class="intro-panel__pitch"><strong>Best leads, best prices</strong> with high volume &amp; quality capacity! Leads from a trusted partner that is <strong>Quik</strong> to use!</p>
    <div class="intro-panel__sign">
      <p class="intro-panel__name">Marcus Delaney</p>
      <address class="intro-panel__role">President,<br>Quik Path Prospects</address>
    </div>
  </div>

  <div class="back-brand">Quik Path Prospects</div>

  <div class="test-banner">TEST OUR LEADS</div>
  <div class="growth">
    <p class="growth__start">Start at 250 or 500 leads.</p>
    <p class="growth__scale">Grow to 1,000...3,000 or evem 10,000!</p>
    <p class="growth__support">We give the right to support your growth.</p>
  </div>

  <div class="intro-copy">
    <h2 class="intro-copy__heading">I want to personally introduce <em>you</em> to our company!</h2>
    <div class="intro-copy__text">
      <p>My team has 50 years of cumulative SSD experience.</p>
      <p>We have proven technology that delivers the best leads.</p>
      <p>The timing is right for a new competitor in this industry.</p>
      <p>I chose to come out of retirement after 30 years with Northfield Industries, the opportunity is just great... I love building businesses and working with great customers!</p>
      <p>Our business, industry, &amp; technical acumen is unrivaled... and we do it at a cost than no others can.</p>
    </div>
  </div>

  <div class="mail-zone">
    <address class="mail-zone__address">Marcus Delaney, President Quik Path Prospects<br>4120 Harbor Lane, Suite 300<br>Dayton, OH 45402</address>
    <div class="mail-zone__stamp"></div>
  </div>
</section>

</body>
</html>
```